Introduction:
We are an Australia-based Cyber Security Penetration testing company seeking a website redesign to showcase our services, expertise, and experience. Our target audience includes businesses and organizations of all sizes who are seeking to secure their IT infrastructure against cyber threats. The purpose of the website redesign is to increase our online presence, generate leads, and establish our company as a trusted authority in the industry.
Objectives:
Create a professional and modern website that is easy to navigate and user-friendly.
Provide information about our company, services, and expertise.
Clearly display table of our 3 services: Bug Bounty as a Service, Penetration Testing and Code Review.
Generate leads through online contact forms and calls-to-action.
Optimize the website for search engines to increase visibility and traffic.
Website similar to: https://www.velmora.com.au/.
Target Audience:
Our target audience includes businesses and organizations of all sizes that require cybersecurity penetration testing services. These include:
Small and medium-sized enterprises (SMEs)
Australian Government agencies
Design Requirements:
Clean, modern, and professional design.
Use of colors that convey trust, reliability, and expertise (such as orange and grey).
Calls-to-action that encourage visitors to contact us or request a quote.
Integration with social media channels to increase engagement and brand awareness.
A blog section to showcase our thought leadership and expertise.
A news section to share updates about our company and the industry.
Content Requirements:
Home page that introduces our company and services and highlights our expertise.
About Us page that provides information about our company, team, and values.
Services page that lists our services and explains the benefits of each.
Case Studies page that showcases our previous work and success stories.
Contact Us page that includes a contact form, phone number, and email address.
Blog section with articles related to the cybersecurity industry and our services.
News section with updates about our company and the industry.

```html
<!DOCTYPE html>
<html lang="en">
<head>
<meta charset="utf-8">
<title>Emberstrata — Cyber Security Penetration Testing</title>
<link href="https://fonts.googleapis.com/css2?family=Rajdhani:wght@600;700&family=Roboto:wght@400;500&display=swap" rel="stylesheet">
<style>
:root{
  --orange:#ee6a3f;
  --ink:#111111;
  --text:#333333;
  --muted:#8a8a8a;
  --dark:#2b2b2d;
  --darker:#232325;
  --line:#cfcfcf;
  --footer:#f2f2f2;
  --white:#ffffff;
}
*{margin:0;padding:0;box-sizing:border-box}
html,body{width:1200px;height:3914px;overflow:hidden;background:var(--white)}
body{font-family:"Roboto",Arial,sans-serif;color:var(--text)}
.page{position:relative;width:1200px;height:3914px;overflow:hidden}
.abs{position:absolute}
.heading{font-family:"Rajdhani",Arial,sans-serif;font-weight:700;color:var(--ink)}
.btn{position:absolute;display:flex;align-items:center;justify-content:center;background:var(--orange);color:var(--white);font-family:"Rajdhani",Arial,sans-serif;font-weight:700;border-radius:30px}

/* header */
.topline{left:0;top:0;width:1200px;height:4px;background:#5a5a5a}
.brand{left:149px;top:70px;font-family:"Rajdhani",Arial,sans-serif;font-weight:700;font-size:34px;color:var(--orange);display:flex;align-items:center;gap:10px}
.brand .dot{width:22px;height:22px;border-radius:50%;background:var(--orange)}
.callus{left:757px;top:24px;display:flex;align-items:center;gap:10px;font-family:"Rajdhani",Arial,sans-serif;font-weight:700;font-size:12px;line-height:15px;color:var(--ink)}
.call-icon{width:34px;height:34px;border-radius:50%;background:var(--orange);display:flex;align-items:center;justify-content:center}
.quote-top{left:899px;top:15px;width:155px;height:50px;font-size:14px}
.nav{left:0;top:88px;width:1200px;height:24px}
.nav a{position:absolute;transform:translateX(-50%);font-family:"Rajdhani",Arial,sans-serif;font-weight:700;font-size:17px;color:#333;text-decoration:none;white-space:nowrap}
.nav a.active{color:var(--orange)}

/* hero */
.hero{left:0;top:137px;width:1200px;height:607px;background:radial-gradient(ellipse at 68% 38%,#e6e6e6 0%,#9a9a9a 28%,#5c5c5c 55%,#3e3e3e 100%)}
.hero-title{left:129px;top:300px;font-size:45px;line-height:53px;color:var(--white)}
.hero-sub{left:129px;top:418px;width:360px;font-weight:500;font-size:17px;line-height:23px;color:var(--white)}
.hero-btn{left:129px;top:488px;width:175px;height:53px;font-size:16px}

/* section titles */
.sec-title{left:0;width:1200px;text-align:center;font-size:52px}
.sec-sub{left:270px;width:660px;text-align:center;font-size:13.5px;line-height:17px;color:var(--muted)}

/* services */
.card{width:280px;height:338px;top:1082px;border:1.5px solid var(--orange);background:var(--white);box-shadow:0 4px 10px rgba(0,0,0,.08);overflow:hidden}
.card-photo{position:absolute;left:33px;top:-73px;width:213px;height:213px;border-radius:50%}
.card-title{position:absolute;left:0;top:168px;width:100%;text-align:center;font-family:"Rajdhani",Arial,sans-serif;font-weight:700;font-size:22px;line-height:20px;color:var(--ink)}
.card-text{position:absolute;left:28px;top:222px;width:224px;text-align:center;font-size:11.5px;line-height:17px;color:#555}
.card-btn{position:absolute;left:71px;bottom:0;width:137px;height:42px;background:var(--orange);border-radius:70px 70px 0 0;color:var(--white);font-family:"Rajdhani",Arial,sans-serif;font-weight:700;font-size:16px;display:flex;align-items:center;justify-content:center;padding-top:6px}
.card-photo-wrap{position:absolute;top:1010px;width:213px;height:213px;border-radius:50%}

/* about */
.about-title{left:655px;top:1796px;font-size:52px;color:var(--white)}
.about-text{left:655px;top:1870px;width:390px;font-size:13.5px;line-height:18px;color:#f0f0f0}
.about-btn{left:655px;top:2057px;width:136px;height:50px;font-size:16px}

/* expertise */
.exp{top:2514px;width:140px;height:155px;border:1.5px solid var(--line);background:var(--white);display:flex;flex-direction:column;align-items:center}
.exp svg{margin-top:28px}
.exp span{margin-top:14px;text-align:center;font-size:15px;line-height:21px;color:#333}

/* contact */
.touch-title{left:0;top:2985px;width:1200px;text-align:center;font-size:52px;color:var(--white)}
.touch-sub{left:290px;width:620px;top:3052px;text-align:center;font-size:13.5px;line-height:18px;color:#cfcfcf}
.field{background:var(--white);font-size:10.5px;font-weight:500;color:#9a9a9a;padding:12px 0 0 14px;letter-spacing:.3px}
.submit{left:526px;top:3292px;width:148px;height:56px;font-size:17px}

/* footer */
.foot-h{font-family:"Rajdhani",Arial,sans-serif;font-weight:700;font-size:23px;color:#333}
.foot-links a{position:absolute;font-size:13px;color:#111;text-decoration:none;white-space:nowrap}
.foot-brand{left:0;width:1200px;top:3718px;text-align:center;font-family:"Rajdhani",Arial,sans-serif;font-weight:700;font-size:46px;color:var(--orange)}
.social{top:3794px;width:20px;height:20px;border-radius:50%;border:2px solid #222}
.contact-row{left:784px;display:flex;align-items:center;gap:12px;font-size:13px;line-height:16px;color:#111}
.contact-icon{width:36px;height:36px;border-radius:50%;border:2px solid var(--orange);display:flex;align-items:center;justify-content:center;flex:none}
.copyright{left:0;width:1200px;top:3856px;text-align:center;font-size:12.5px;color:#111}
</style>
</head>
<body>
<div class="page">

  <!-- header -->
  <div class="abs topline"></div>
  <div class="abs brand"><span class="dot"></span>Emberstrata</div>
  <div class="abs callus">
    <div class="call-icon"><svg width="16" height="16" viewBox="0 0 24 24"><path fill="#fff" d="M6.6 10.8a15 15 0 0 0 6.6 6.6l2.2-2.2c.3-.3.7-.4 1-.2 1.1.4 2.3.6 3.6.6.6 0 1 .4 1 1V20c0 .6-.4 1-1 1A17 17 0 0 1 3 4c0-.6.4-1 1-1h3.5c.6 0 1 .4 1 1 0 1.3.2 2.5.6 3.6.1.3 0 .7-.2 1z"/></svg></div>
    <div>Call Us<br>555-014-2270</div>
  </div>
  <div class="btn quote-top">Request a Quote</div>
  <nav class="abs nav">
    <a class="active" style="left:425px">Home</a>
    <a style="left:516px">About Us</a>
    <a style="left:617px">Services</a>
    <a style="left:732px">Case Studies</a>
    <a style="left:857px">Contact Us</a>
    <a style="left:949px">Blog</a>
    <a style="left:1025px">News</a>
  </nav>

  <!-- hero -->
  <div class="abs hero" role="img" aria-label="Monochrome photo of a hand holding a glowing cloud with a lock inside a network of connected points"></div>
  <svg class="abs" style="left:0;top:600px" width="1200" height="145" viewBox="0 0 1200 145">
    <path fill="#fff" d="M0,128 Q110,95 215,135 C290,30 560,40 630,110 C710,40 980,40 1060,140 Q1130,110 1200,115 L1200,145 L0,145 Z"/>
  </svg>
  <h1 class="abs heading hero-title">Cyber Security<br>Penetration testing</h1>
  <p class="abs hero-sub">Lorem ipsum dolor sit amet, cons ectetur adipiscinpsum dolor sit ame do.</p>
  <div class="btn hero-btn">Request a Quote</div>

  <!-- services -->
  <h2 class="abs heading sec-title" style="top:868px">Our Services</h2>
  <p class="abs sec-sub" style="top:943px">Lorem ipsum dolor sit amet, consectetur adipiscing elit, sed do eiusmod tempor incididunt ut labore et dolore magna aliqua. Quis ipsum suspendisse ultrices gravida. Risus commodo viverra mae</p>

  <div class="abs card" style="left:147px">
    <div class="card-title">Bug Bounty as<br>a Service</div>
    <p class="card-text">Lorem ipsum dolor sit amet, consectetur adipiscing elit, sed do eiusmod tempor incididunt ut labore et dolore ma.</p>
    <div class="card-btn">Read More</div>
  </div>
  <div class="abs card" style="left:460px">
    <div class="card-title">Penetration Testing</div>
    <p class="card-text">Lorem ipsum dolor sit amet, consectetur adipiscing elit, sed do eiusmod tempor incididunt ut labore et dolore ma.</p>
    <div class="card-btn">Read More</div>
  </div>
  <div class="abs card" style="left:773px">
    <div class="card-title">Code Review</div>
    <p class="card-text">Lorem ipsum dolor sit amet, consectetur adipiscing elit, sed do eiusmod tempor incididunt ut labore et dolore ma.</p>
    <div class="card-btn">Read More</div>
  </div>
  <div class="card-photo-wrap" style="left:184px;background:radial-gradient(circle at 45% 40%,#ff6a4a,#c4241a 60%,#4a0d0a)" role="img" aria-label="Red illustration of a magnifying glass over a bug on a laptop"></div>
  <div class="card-photo-wrap" style="left:497px;background:radial-gradient(circle at 50% 50%,#2a8fd6,#0f3f6e 60%,#061626)" role="img" aria-label="Businessman behind a glowing blue security shield interface"></div>
  <div class="card-photo-wrap" style="left:810px;background:radial-gradient(circle at 40% 40%,#6a6f86,#2a2c3a 60%,#0c0c12)" role="img" aria-label="Close-up of hands typing code on a laptop keyboard"></div>

  <!-- about -->
  <svg class="abs" style="left:0;top:1560px" width="1200" height="680" viewBox="0 0 1200 680" role="img" aria-label="Dark photo of a login screen with username and password fields">
    <defs><linearGradient id="aboutBg" x1="0" y1="0" x2="1" y2="1"><stop offset="0" stop-color="#3a3a3c"/><stop offset=".5" stop-color="#2c2c2e"/><stop offset="1" stop-color="#252527"/></linearGradient></defs>
    <path fill="url(#aboutBg)" d="M0,112 C150,40 330,-10 520,20 C680,45 760,140 900,140 C1010,140 1100,120 1200,115 L1200,565 C1120,620 1000,670 800,670 C620,670 500,580 360,560 C200,540 80,540 0,552 Z"/>
  </svg>
  <h2 class="abs heading about-title">About Us</h2>
  <p class="abs about-text">Lorem ipsum dolor sit amet, consectetur adipiscing elised do eiusmLorem ipsum dolor sit amet, consectetur adipisci ng elit, sed do eiusmod tempor incididunt ut labore et dolore magna aliqua. Ut enim ad minim veniam, quis nostrulored exercitation ullamco laboris nisi ut aliquip ex ea commodo consequat. Duis aute irure dolor in reprehenderit in voluptate velit esseod tempor incididunt ut labore et dolore magna aliqua. Ut enim ad minim veniaquis nostrud exercitation ullamco laboris nisi ut aliquip ex ea.</p>
  <div class="btn about-btn">Read More</div>

  <!-- expertise -->
  <h2 class="abs heading sec-title" style="top:2349px">We Expertise</h2>
  <p class="abs sec-sub" style="top:2424px">Lorem ipsum dolor sit amet, consectetur adipiscing elit, sed do eiusmod tempor incididunt ut labore et dolore magna aliqua. Quis ipsum suspendisse ultrices gravida. Risus commodo viverra mae</p>

  <div class="abs exp" style="left:149px">
    <svg width="48" height="48" viewBox="0 0 48 48" fill="none" stroke="#ee6a3f" stroke-width="2"><path d="M6 16h36l-3-8H9z"/><path d="M6 16v4a6 6 0 0 0 12 0 6 6 0 0 0 12 0 6 6 0 0 0 12 0v-4"/><path d="M9 26v16h30V26"/><rect x="20" y="32" width="8" height="10"/></svg>
    <span>Retail &amp;<br>Ecommerce</span>
  </div>
  <div class="abs exp" style="left:301px">
    <svg width="48" height="48" viewBox="0 0 48 48" fill="none" stroke="#ee6a3f" stroke-width="2"><path d="M4 42h40"/><rect x="8" y="30" width="6" height="12"/><rect x="18" y="24" width="6" height="18"/><rect x="28" y="26" width="6" height="16"/><rect x="38" y="18" width="5" height="24"/><path d="M8 24l10-6 10 4 10-10"/><circle cx="40" cy="8" r="5"/></svg>
    <span>Finance</span>
  </div>
  <div class="abs exp" style="left:453px">
    <svg width="48" height="48" viewBox="0 0 48 48" fill="none" stroke="#ee6a3f" stroke-width="2"><path d="M24 4v10M24 4h8v5h-8"/><path d="M8 22l16-8 16 8z"/><path d="M10 22v16M17 24v14M24 24v14M31 24v14M38 22v16"/><path d="M4 42h40M6 38h36"/></svg>
    <span>Government</span>
  </div>
  <div class="abs exp" style="left:605px">
    <svg width="48" height="48" viewBox="0 0 48 48" fill="none" stroke="#ee6a3f" stroke-width="2"><path d="M24 22s-10-6-10-12a5 5 0 0 1 10-1 5 5 0 0 1 10 1c0 6-10 12-10 12z"/><path d="M4 24l6 10 8 4v6M44 24l-6 10-8 4v6"/><path d="M10 34l6-6M38 34l-6-6"/></svg>
    <span>Healthcare</span>
  </div>
  <div class="abs exp" style="left:757px">
    <svg width="48" height="48" viewBox="0 0 48 48" fill="none" stroke="#ee6a3f" stroke-width="2"><rect x="6" y="12" width="36" height="24" rx="2"/><path d="M2 40h44"/><circle cx="24" cy="24" r="5"/><path d="M24 15v3M24 30v3M15 24h3M30 24h3"/><circle cx="34" cy="8" r="4"/></svg>
    <span>Technology</span>
  </div>
  <div class="abs exp" style="left:909px">
    <svg width="48" height="48" viewBox="0 0 48 48" fill="none" stroke="#ee6a3f" stroke-width="2"><path d="M18 22l12-10 12 10v20H18z"/><path d="M31 24l-4 8h5l-3 7"/><path d="M8 6v8M14 6v8M6 14h10v6a5 5 0 0 1-10 0z"/><path d="M11 25v17h7"/></svg>
    <span>Utilities and<br>Energy</span>
  </div>

  <!-- get in touch -->
  <svg class="abs" style="left:0;top:2800px" width="1200" height="770" viewBox="0 0 1200 770" role="img" aria-label="Dark night city skyline overlaid with a network of connected points">
    <defs><linearGradient id="touchBg" x1="0" y1="0" x2="0" y2="1"><stop offset="0" stop-color="#2a2a2a"/><stop offset=".55" stop-color="#363636"/><stop offset="1" stop-color="#262626"/></linearGradient></defs>
    <path fill="url(#touchBg)" d="M0,90 C70,65 170,68 225,88 C290,10 560,10 625,85 C690,40 820,45 860,80 C950,30 1130,40 1200,95 L1200,700 C1120,740 1000,735 960,710 C900,760 720,760 660,720 C610,765 450,765 400,725 C340,760 200,755 160,720 C110,745 40,740 0,720 Z"/>
  </svg>
  <h2 class="abs heading touch-title">Get in Touch</h2>
  <p class="abs touch-sub">Lorem ipsum dolor sit amet, consectetur adipiscing elit, sed do eiusmod tempor incididunt ut labore et dolore magna aliqua. Quis ipsum suspendisse ultrices gravida.</p>
  <div class="abs field" style="left:246px;top:3140px;width:222px;height:35px">NAME</div>
  <div class="abs field" style="left:483px;top:3140px;width:223px;height:35px">PHONE</div>
  <div class="abs field" style="left:723px;top:3140px;width:229px;height:35px">EMAIL</div>
  <div class="abs field" style="left:246px;top:3199px;width:708px;height:112px">MESSAGE</div>
  <div class="btn submit">SUBMIT</div>

  <!-- footer -->
  <div class="abs" style="left:0;top:3562px;width:1200px;height:352px;background:var(--footer);z-index:-1"></div>
  <div class="abs foot-h" style="left:150px;top:3630px">Links</div>
  <div class="abs foot-links" style="left:0;top:0">
    <a style="left:155px;top:3686px">Home</a>
    <a style="left:155px;top:3711px">About Us</a>
    <a style="left:155px;top:3736px">Services</a>
    <a style="left:155px;top:3761px">Case Studies</a>
    <a style="left:155px;top:3786px">Contact Us</a>
    <a style="left:269px;top:3686px">Blog</a>
    <a style="left:269px;top:3711px">News</a>
    <a style="left:269px;top:3736px">Bug Bounty</a>
    <a style="left:269px;top:3761px">Penetration Testing</a>
    <a style="left:269px;top:3786px">Code Review.</a>
  </div>
  <div class="abs foot-brand">Emberstrata</div>
  <div class="abs social" style="left:550px" aria-label="Social profile"></div>
  <div class="abs social" style="left:585px" aria-label="Social profile"></div>
  <div class="abs social" style="left:625px" aria-label="Social profile"></div>

  <div class="abs foot-h" style="left:784px;top:3630px">Contact</div>
  <div class="abs contact-row" style="top:3675px">
    <div class="contact-icon"><svg width="14" height="16" viewBox="0 0 24 28"><path fill="#ee6a3f" d="M12 0a10 10 0 0 0-10 10c0 7.5 10 18 10 18s10-10.5 10-18A10 10 0 0 0 12 0zm0 14a4 4 0 1 1 0-8 4 4 0 0 1 0 8z"/></svg></div>
    <div>Address: ingo Lorem 677<br>Lorem ipsum dumys</div>
  </div>
  <div class="abs contact-row" style="top:3725px">
    <div class="contact-icon"><svg width="15" height="15" viewBox="0 0 24 24"><path fill="#ee6a3f" d="M6.6 10.8a15 15 0 0 0 6.6 6.6l2.2-2.2c.3-.3.7-.4 1-.2 1.1.4 2.3.6 3.6.6.6 0 1 .4 1 1V20c0 .6-.4 1-1 1A17 17 0 0 1 3 4c0-.6.4-1 1-1h3.5c.6 0 1 .4 1 1 0 1.3.2 2.5.6 3.6.1.3 0 .7-.2 1z"/></svg></div>
    <div>Phone:(09) 555 010 482,</div>
  </div>
  <div class="abs contact-row" style="top:3775px">
    <div class="contact-icon"><svg width="16" height="12" viewBox="0 0 24 18"><path fill="#ee6a3f" d="M0 0h24v18H0z"/><path fill="none" stroke="#fff" stroke-width="2" d="M1 1l11 9 11-9"/></svg></div>
    <div>Email:info@emberstrata.com</div>
  </div>
  <p class="abs copyright">Copyright © 2023&nbsp; All rights reserved.</p>
</div>
</body>
</html>
```